Artistic Poster for Magic Show

I need a poster for a small theater magic show that will tour in Switzerland.
It will hang in towns outside and inside! It needs to jump out, but be intressting, have admosphere and be classy!! The show is all about magic from the victorian times. But its a contemporary show. So the poster needs to show that its not a clichè magic show they will see. The name means collection of wonderfull curiosity's. It needs to contain the following Text:
Name of the show: " Seltsame Gezeitenspiele"
Name artist: Lukas Brenninger
Description; Eine Fesselnde Zaubervostellung
It needs a place for date, time, city and name of theater.
Hereby you will find some examples of posters we like and the style we like. Also pictures to use and two PNG files. Thank you a lot and looking forward to see your result!! Best wishes Lukas Brenninger

Target Market(s)

Theater visiting public.

Industry/Entity Type

Entertainment

Font styles to use
Serif
Decorative
Script

Requirements
Must have
• A picture of the artist. Text.
Nice to have
• Something that is a bit magicall, a optical illusion, but minimalistic...
Should not have
• It is contamporary magic. It should show that they will not watch a stereotype magic show.

```html
<!DOCTYPE html>
<html lang="de">
<head>
<meta charset="utf-8">
<title>Seltsame Gezeitenspiele – Poster</title>
<link rel="stylesheet" href="https://fonts.googleapis.com/css2?family=Sancreek&family=Oswald:wght@600&family=Marcellus&family=Fira+Sans:wght@500&display=swap">
<style>
  :root {
    --ink-dark: #140f0c;
    --smoke-brown: #4a3624;
    --warm-gold: #b38a52;
    --cream: #fbf8ee;
    --title-red: #ee1c1c;
    --date-pale: #fde28c;
    --date-orange: #f7a531;
    --badge-gold: #c9a047;
  }
  html, body {
    margin: 0;
    padding: 0;
    overflow: hidden;
    background: var(--ink-dark);
  }
  .poster {
    position: relative;
    width: 900px;
    height: 1200px;
    overflow: hidden;
    background: var(--ink-dark);
  }
  .artist-photo {
    position: absolute;
    inset: 0;
    background:
      radial-gradient(ellipse 260px 360px at 770px 640px, #c9936b 0%, #8a5a3c 35%, rgba(60,40,28,0) 75%),
      radial-gradient(ellipse 520px 260px at 650px 60px, #b99058 0%, rgba(120,88,52,0.5) 50%, rgba(0,0,0,0) 80%),
      radial-gradient(ellipse 400px 320px at 120px 80px, #8d6a3e 0%, rgba(0,0,0,0) 75%),
      radial-gradient(ellipse 320px 380px at 380px 540px, #3a2a1d 0%, rgba(0,0,0,0) 80%),
      linear-gradient(180deg, #5b4329 0%, #2a1e15 35%, #1a130e 70%, #2b2018 100%);
  }
  .show-title {
    position: absolute;
    left: 0;
    width: 900px;
    text-align: center;
    margin: 0;
    font-family: "Sancreek", "Rye", serif;
    font-weight: 400;
    color: var(--cream);
    line-height: 1;
    text-shadow: -14px -10px 0 rgba(20, 14, 10, 0.75);
  }
  .show-title .line-one {
    position: absolute;
    top: 52px;
    left: 0;
    width: 900px;
    font-size: 110px;
  }
  .show-title .line-two {
    position: absolute;
    top: 186px;
    left: 0;
    width: 900px;
    font-size: 90px;
    letter-spacing: 1px;
  }
  .tagline {
    position: absolute;
    top: 348px;
    left: 0;
    width: 900px;
    text-align: center;
    margin: 0;
    font-family: "Sancreek", "Rye", serif;
    font-size: 42px;
    color: var(--title-red);
    letter-spacing: 1px;
  }
  .event-info {
    position: absolute;
    left: 48px;
    top: 478px;
  }
  .dates {
    margin: 0;
    font-family: "Oswald", sans-serif;
    font-weight: 600;
    font-size: 140px;
    line-height: 1;
  }
  .dates .day-one { color: var(--date-pale); }
  .dates .day-two { color: var(--date-orange); }
  .month {
    margin: 0;
    font-family: "Marcellus", serif;
    font-size: 66px;
    line-height: 1;
    color: var(--cream);
    margin-top: -4px;
  }
  .time, .venue {
    margin: 0;
    font-family: "Fira Sans", sans-serif;
    font-weight: 500;
    font-size: 40px;
    line-height: 1.25;
  }
  .time { color: var(--date-pale); margin-top: 38px; }
  .venue { color: var(--date-orange); }
  .artist-name {
    position: absolute;
    left: 54px;
    top: 872px;
    margin: 0;
    font-family: "Marcellus", serif;
    font-size: 88px;
    line-height: 1;
    color: var(--cream);
  }
  .award-badge {
    position: absolute;
    top: 1010px;
    width: 180px;
    height: 180px;
  }
  .award-badge.left { left: 40px; }
  .award-badge.right { left: 675px; }
</style>
</head>
<body>
  <main class="poster">
    <div class="artist-photo" role="img" aria-label="Fotografie des Künstlers mit Zylinder und Zwirbelbart, den Hut grüßend, umhüllt von warmem Rauch"></div>

    <h1 class="show-title">
      <span class="line-one">Seltsame</span>
      <span class="line-two">Gezeitenspiele</span>
    </h1>
    <p class="tagline">Eine Fesselnde Zaubervostellung</p>

    <section class="event-info">
      <p class="dates"><span class="day-one">23</span><span class="day-one">,</span><span class="day-two">24</span></p>
      <p class="month">November</p>
      <p class="time">8:00pm</p>
      <p class="venue">Lindenhoftheater<br>Berna</p>
    </section>

    <p class="artist-name">Lukas Brenninger</p>

    <svg class="award-badge left" viewBox="0 0 180 180" aria-label="Auszeichnung">
      <circle cx="90" cy="90" r="82" fill="none" stroke="var(--badge-gold)" stroke-width="5"/>
    </svg>
    <svg class="award-badge right" viewBox="0 0 180 180" aria-label="Auszeichnung">
      <circle cx="90" cy="90" r="82" fill="none" stroke="var(--badge-gold)" stroke-width="5"/>
    </svg>
  </main>
</body>
</html>
```